Harbor HVAC Contractors - Ductless Mini-Split Ad Creative Brief 4 cp ad images

Our Offers (Must Be Clearly Visible in the Design)
100% Satisfaction Guarantee
"We guarantee to keep you cool, or your money back! If you're not happy after we’ve had a chance to fix it, we’ll refund you!"

5-Year Labor Warranty
"That’s right – a 5-year labor warranty! No maintenance agreement required, just clean your filters each month!"

Chill-Wave Season 2026
"LIMITED-TIME OFFER: Get $999 off any ductless mini-split installation!"

Transparent Pricing
"What you see is what you pay—NO hidden fees!"

Ad Design Guidelines
Primary Focus: Ductless Mini-Split A/C Systems ONLY
Color Scheme: Must incorporate Harbor HVAC Contractors' main colors with a hint of yellow to catch attention.
Look at truck wrap to get a feel for the border of ad image creative
Branding Elements: Include Harbor HVAC logo prominently.
Contact Details: Display phone number clearly.
Trust Builders: Feature Chatterpage & Zintrova review elements to enhance credibility.
Visibility: The offers must be clear and readable but not overcrowded. Prioritize readability and clean design.
Final Notes
Ensure the design is high-converting and visually engaging while maintaining a professional, premium feel.
The ad creatives will be used for ductless mini-split A/C systems only—this must be clear in the design messaging.
Feel Free to use your expertise and experience to make this better
Thank you 555-203-7148

```html
<!DOCTYPE html>
<html lang="en">
<head>
<meta charset="utf-8">
<title>Harbor HVAC Contractors – Ductless Mini-Split Ads</title>
<link rel="stylesheet" href="https://fonts.googleapis.com/css2?family=Lexend:wght@600;700;800&family=Outfit:wght@400;500;600;700&display=swap">
<style>
  :root {
    --stage: #8aa9d4;
    --white: #ffffff;
    --ink: #2a2a2e;
    --red: #c1272d;
    --navy: #2f5aa0;
    --deep-blue: #1f4f9c;
    --sky: #2aa7ff;
    --sky-soft: #9fd4ff;
    --yellow: #f7d21e;
    --star: #f5b82e;
    --pink-soft: #f2c6cc;
    --wall: #d9d4ca;
  }
  * { box-sizing: border-box; margin: 0; padding: 0; }
  html, body { width: 1200px; height: 652px; overflow: hidden; }
  body { background: var(--stage); font-family: "Outfit", sans-serif; position: relative; }

  .ad { position: absolute; top: 62px; width: 528px; height: 528px; overflow: hidden; }
  .ad--guarantee { left: 64px; background: var(--white); }
  .ad--warranty { left: 609px; }

  /* decorative shapes */
  .deco { position: absolute; }
  .blob-top { right: -50px; top: -60px; width: 240px; height: 220px; border-radius: 50%;
    background: radial-gradient(circle at 40% 45%, var(--sky) 0%, #5fc0ff 50%, rgba(160,215,255,0) 72%); }
  .fan-graphic { left: -20px; top: 325px; width: 110px; height: 110px; border-radius: 50%;
    background: radial-gradient(circle, #3aa6ff 0%, #7cc6ff 55%, rgba(160,215,255,0) 72%); }
  .swoosh { left: 0; top: 0; width: 528px; height: 528px; }

  .photo {
    position: absolute; left: 31px; top: 54px; width: 228px; height: 292px;
    border: 5px solid var(--white); box-shadow: 0 4px 12px rgba(0,0,0,.22);
    transform: rotate(-2deg);
    background: linear-gradient(160deg, #cbbfa6 0%, #8c8f93 50%, #3d4f6b 80%, #4e7a3a 100%);
  }

  .headline { position: absolute; left: 268px; top: 102px; font-family: "Lexend", sans-serif; line-height: 1; color: var(--ink); }
  .headline__pct { display: block; font-size: 52px; font-weight: 800; letter-spacing: -2.5px;
    background: linear-gradient(90deg, var(--red), var(--navy)); -webkit-background-clip: text; background-clip: text; color: transparent; }
  .headline__line { display: block; font-size: 40px; font-weight: 700; letter-spacing: -1px; margin-top: 6px;
    transform: rotate(-2.5deg); transform-origin: left; }

  .promise {
    position: absolute; left: 248px; top: 290px; width: 226px; height: 86px; border-radius: 4px;
    background: linear-gradient(90deg, var(--red), var(--navy));
    color: var(--white); font-size: 16.5px; font-weight: 500; line-height: 1.12; padding: 14px 16px 0 20px; letter-spacing: -.4px;
  }
  .tick { position: absolute; left: 451px; top: 262px; width: 46px; height: 46px; }

  .brand { position: absolute; display: flex; align-items: center; gap: 7px; font-weight: 700; }
  .brand__dot { width: 30px; height: 30px; border-radius: 50%; flex: none; }
  .brand__name { font-size: 17px; line-height: 1.05; letter-spacing: .5px; }
  .ad--guarantee .brand { left: 36px; top: 462px; color: var(--navy); }
  .ad--guarantee .brand__dot { background: var(--red); }
  .ad--warranty .brand { left: 330px; top: 414px; color: var(--white); }
  .ad--warranty .brand__dot { background: var(--white); }

  .ratings { position: absolute; display: flex; gap: 14px; }
  .rating { display: flex; align-items: center; gap: 5px; }
  .rating__mark { width: 28px; height: 28px; border-radius: 50%; flex: none; }
  .rating__body { display: flex; flex-direction: column; line-height: 1; }
  .rating__name { font-size: 9px; font-weight: 600; }
  .rating__stars { color: var(--star); font-size: 11px; letter-spacing: 1px; }
  .rating__score { font-size: 8.5px; font-weight: 700; letter-spacing: 1px; margin-top: 2px; }
  .ad--guarantee .ratings { left: 306px; top: 409px; color: #444; }
  .ad--guarantee .rating__mark { background: var(--deep-blue); }
  .ad--warranty .ratings { left: 38px; top: 367px; color: var(--white); }
  .ad--warranty .rating__mark { background: var(--white); }

  .contact { position: absolute; font-size: 16px; line-height: 1; }
  .contact__row { display: flex; align-items: center; gap: 7px; }
  .contact__row + .contact__row { margin-top: 11px; }
  .contact svg { width: 12px; height: 12px; flex: none; }
  .ad--guarantee .contact { left: 306px; top: 454px; color: var(--ink); }
  .ad--warranty .contact { left: 332px; top: 464px; color: var(--white); font-size: 14px; }
  .ad--warranty .contact__row + .contact__row { margin-top: 8px; }

  /* warranty ad */
  .scene-photo { position: absolute; inset: 0;
    background: linear-gradient(180deg, var(--wall) 0%, #cfc9be 45%, #6d6a6a 65%, #2c2f3a 80%); }
  .scene-fade { position: absolute; left: 0; right: 0; bottom: 0; height: 210px;
    background: linear-gradient(180deg, rgba(31,79,156,0) 0%, rgba(31,79,156,.85) 45%, var(--deep-blue) 100%); }
  .tag-year { position: absolute; left: 179px; top: 50px; width: 172px; height: 63px;
    background: linear-gradient(90deg, var(--red), var(--navy)); transform: rotate(-1deg);
    color: var(--white); font-family: "Lexend", sans-serif; font-weight: 800; font-size: 47px; letter-spacing: -2.5px;
    display: flex; align-items: center; justify-content: center; }
  .tag-label { position: absolute; left: 112px; top: 110px; width: 297px; height: 62px; background: var(--white);
    border: 1px solid var(--navy); border-radius: 3px; transform: rotate(1.5deg);
    color: var(--ink); font-family: "Lexend", sans-serif; font-weight: 700; font-size: 36px; letter-spacing: -1.2px;
    display: flex; align-items: center; justify-content: center; }
  .offer { position: absolute; left: 38px; top: 406px; width: 250px; color: var(--white);
    font-size: 16.5px; font-weight: 500; line-height: 1.13; letter-spacing: -.5px; white-space: nowrap; }
  .offer__hl { color: var(--yellow); }
  .divider { position: absolute; left: 300px; top: 423px; width: 1px; height: 74px; background: rgba(255,255,255,.8); }
</style>
</head>
<body>

<section class="ad ad--guarantee" aria-label="Satisfaction guarantee ad">
  <div class="deco blob-top"></div>
  <svg class="deco swoosh" viewBox="0 0 528 528" aria-hidden="true">
    <path d="M220 400 C330 360 440 380 528 300 L528 330 C450 400 340 390 220 400Z" fill="var(--pink-soft)" opacity=".7"/>
    <path d="M470 370 C500 360 520 380 528 390 L528 420 C510 400 490 390 470 370Z" fill="var(--sky-soft)" opacity=".6"/>
  </svg>
  <div class="deco fan-graphic" role="img" aria-label="Blue fan blade graphic"></div>

  <div class="photo" role="img" aria-label="Homeowner and technician standing beside an outdoor AC unit"></div>

  <h1 class="headline">
    <span class="headline__pct">100%</span>
    <span class="headline__line">Satisfaction</span>
    <span class="headline__line">Guarantee</span>
  </h1>

  <p class="promise">We guarantee to keep<br>you cool, or your money<br>back!</p>
  <svg class="tick" viewBox="0 0 46 46" aria-hidden="true">
    <circle cx="23" cy="23" r="22" fill="#f4f6f2" stroke="#dfe3dc"/>
    <path d="M11 23 L20 32 L37 14" fill="none" stroke="var(--yellow)" stroke-width="6" stroke-linecap="round" stroke-linejoin="round"/>
  </svg>

  <div class="brand">
    <span class="brand__dot"></span>
    <span class="brand__name">HARBOR HVAC<br>CONTRACTORS</span>
  </div>

  <div class="ratings">
    <div class="rating">
      <span class="rating__mark"></span>
      <span class="rating__body"><span class="rating__name">Chatterpage</span><span class="rating__stars">★★★★★</span><span class="rating__score">5.0 RATING</span></span>
    </div>
    <div class="rating">
      <span class="rating__mark"></span>
      <span class="rating__body"><span class="rating__name">Zintrova</span><span class="rating__stars">★★★★★</span><span class="rating__score">5.0 RATING</span></span>
    </div>
  </div>

  <div class="contact">
    <div class="contact__row">
      <svg viewBox="0 0 24 24"><path d="M6.6 10.8a15 15 0 0 0 6.6 6.6l2.2-2.2a1 1 0 0 1 1-.25 11.4 11.4 0 0 0 3.6.57 1 1 0 0 1 1 1V20a1 1 0 0 1-1 1A17 17 0 0 1 3 4a1 1 0 0 1 1-1h3.5a1 1 0 0 1 1 1c0 1.25.2 2.45.57 3.57a1 1 0 0 1-.25 1z" fill="var(--red)"/></svg>
      <span>555-203-7148</span>
    </div>
    <div class="contact__row">
      <svg viewBox="0 0 24 24"><rect x="2" y="5" width="20" height="14" rx="2" fill="var(--deep-blue)"/><path d="M3 6l9 7 9-7" fill="none" stroke="#fff" stroke-width="1.6"/></svg>
      <span>harborhvacservice.com</span>
    </div>
  </div>
</section>

<section class="ad ad--warranty" aria-label="Labor warranty ad">
  <div class="scene-photo" role="img" aria-label="Installation crew standing beside two snow-covered ductless mini-split outdoor units"></div>
  <div class="scene-fade"></div>

  <div class="tag-year">5-Year</div>
  <div class="tag-label">Labor Warranty</div>

  <div class="ratings">
    <div class="rating">
      <span class="rating__mark"></span>
      <span class="rating__body"><span class="rating__name">Chatterpage</span><span class="rating__stars">★★★★★</span><span class="rating__score">5.0 RATING</span></span>
    </div>
    <div class="rating">
      <span class="rating__mark"></span>
      <span class="rating__body"><span class="rating__name">Zintrova</span><span class="rating__stars">★★★★★</span><span class="rating__score">5.0 RATING</span></span>
    </div>
  </div>

  <p class="offer">That’s right - <span class="offer__hl">a 5-year labor<br>warranty! for ductless mini<br>splits a/c.</span> No maintenance<br>agreement required, just<br>clean your filters each month!</p>

  <div class="divider"></div>

  <div class="brand">
    <span class="brand__dot"></span>
    <span class="brand__name">HARBOR HVAC<br>CONTRACTORS</span>
  </div>

  <div class="contact">
    <div class="contact__row">
      <svg viewBox="0 0 24 24"><path d="M6.6 10.8a15 15 0 0 0 6.6 6.6l2.2-2.2a1 1 0 0 1 1-.25 11.4 11.4 0 0 0 3.6.57 1 1 0 0 1 1 1V20a1 1 0 0 1-1 1A17 17 0 0 1 3 4a1 1 0 0 1 1-1h3.5a1 1 0 0 1 1 1c0 1.25.2 2.45.57 3.57a1 1 0 0 1-.25 1z" fill="var(--yellow)"/></svg>
      <span>555-203-7148</span>
    </div>
    <div class="contact__row">
      <svg viewBox="0 0 24 24"><rect x="2" y="5" width="20" height="14" rx="2" fill="var(--yellow)"/><path d="M3 6l9 7 9-7" fill="none" stroke="var(--deep-blue)" stroke-width="1.6"/></svg>
      <span>harborhvacservice.com</span>
    </div>
  </div>
</section>

</body>
</html>
```